I need to rebrand my public user portal for a new/modern look and feel

I want to take my current user web portal and redesign the look of it. I have included 2 samples of my current user portal and would like options to create a new functional look. This main page below will modify based on the tabs on the top left. Any questions please ask.

```html
<!DOCTYPE html>
<html lang="en">
<head>
<meta charset="utf-8">
<title>Northway Learning – Student Portal Dashboard</title>
<link href="https://fonts.googleapis.com/css2?family=Roboto:wght@400;500;700&display=swap" rel="stylesheet">
<style>
:root{
  --page:#f8f8f8;
  --canvas:#f0f0f0;
  --header:#1b1b1b;
  --white:#ffffff;
  --ink:#111111;
  --text:#3c3c3c;
  --teal:#3d97ad;
  --teal-link:#3592a8;
  --alert:#f07272;
  --line:#dcdcdc;
  --highlight:#dbf8fc;
  --field:#ececec;
  --muted:#6a6a6a;
}
*{box-sizing:border-box;margin:0;padding:0}
html,body{width:1200px;height:1200px;overflow:hidden}
body{background:var(--page);font-family:"Roboto",sans-serif;color:var(--text);position:relative}
.portal{position:absolute;left:96px;top:197px;width:1007px;height:805px;background:var(--canvas);box-shadow:0 2px 4px rgba(0,0,0,.25)}
.topbar{position:absolute;left:0;top:0;width:100%;height:70px;background:var(--header);color:var(--white)}
.brand{position:absolute;left:23px;top:0;height:70px;display:flex;align-items:center;gap:8px;font-weight:700;font-size:17px;letter-spacing:.5px;color:var(--white)}
.brand-mark{width:22px;height:22px;border:2px solid var(--white);border-radius:50%}
.nav a{position:absolute;top:26px;font-size:12.5px;color:var(--white);text-decoration:none;line-height:18px}
.nav .active{border-bottom:1px solid var(--teal);padding-bottom:2px}
.bell{position:absolute;left:902px;top:24px;width:24px;height:24px;border-radius:50%;background:#2c2c34;display:flex;align-items:center;justify-content:center}
.avatar{position:absolute;left:938px;top:24px;width:24px;height:24px;border-radius:50%;background:linear-gradient(135deg,#e7b79c,#b46a55)}
.avatar-dot{position:absolute;left:957px;top:24px;width:6px;height:6px;border-radius:50%;background:#3ccf6a}
.chev{position:absolute;left:975px;top:31px}
.org-card{position:absolute;top:107px;width:421px;height:141px;background:var(--white)}
.org-card.left{left:63px}
.org-card.right{left:529px}
.org-logo{position:absolute;top:34px;width:68px;height:68px;border:1.5px solid var(--teal);border-radius:50%;display:flex;align-items:center;justify-content:center;font-size:10px;font-weight:500;color:var(--ink)}
.org-info{position:absolute;top:16px}
.org-name{font-size:21px;font-weight:700;color:var(--ink);line-height:25px}
.org-sub{font-size:12.5px;color:var(--teal-link);line-height:16px}
.org-status{display:flex;align-items:center;gap:6px;margin-top:4px;font-size:16px;color:var(--alert);line-height:20px}
.info-box{width:19px;height:17px;border:1px solid #f4b3b3;font-size:12px;display:flex;align-items:center;justify-content:center}
.btn-add{display:flex;align-items:center;gap:7px;width:163px;height:35px;background:var(--teal);color:var(--white);font-size:12.5px;padding-left:14px}
.org-info .btn-add{margin-top:8px}
.caret{width:0;height:0;border-left:4px solid transparent;border-right:4px solid transparent;border-top:5px solid var(--white)}
.section-label{position:absolute;left:66px;top:261px;font-size:12.5px;color:var(--teal-link)}
.students-panel{position:absolute;left:63px;top:279px;width:887px;height:451px;background:var(--white)}
.panel-title{position:absolute;left:24px;top:19px;font-size:16px;font-weight:700;color:var(--ink)}
.search{position:absolute;left:24px;top:50px;width:172px;height:26px;background:var(--field);display:flex;align-items:center;gap:6px;padding-left:6px;font-size:8px;color:var(--muted)}
.filter{position:absolute;left:207px;top:50px;width:127px;height:26px;background:var(--field);display:flex;align-items:center;justify-content:center;gap:6px;font-size:10.5px;color:var(--muted)}
.students-panel .btn-add{position:absolute;left:701px;top:46px}
.table{position:absolute;left:17px;top:97px;width:846px}
.row{position:relative;border-bottom:1px solid var(--line);font-size:11.5px}
.row.head{height:38px;font-weight:500;color:var(--ink)}
.row.hl{background:var(--highlight)}
.row:last-child{border-bottom:none}
.cell{position:absolute}
.c-name{left:7px}.c-grade{left:195px}.c-year{left:332px}.c-school{left:469px}.c-act{left:692px}
.row.head .cell{top:10px}
.btn-edit{width:113px;height:35px;background:var(--teal);color:var(--white);font-size:12.5px;display:flex;align-items:center;justify-content:center;border-radius:2px}
.pager{position:absolute;left:875px;top:738px;display:flex;align-items:center;gap:6px;font-size:12.5px;color:var(--ink)}
</style>
</head>
<body>
<div class="portal">
  <header class="topbar">
    <div class="brand"><span class="brand-mark"></span>NORTHWAY LEARNING</div>
    <nav class="nav">
      <a class="active" style="left:285px">Dashboard</a>
      <a style="left:382px">Applications</a>
      <a style="left:489px">Transcript Request</a>
      <a style="left:631px">New Hire Packet</a>
    </nav>
    <div class="bell"><svg width="10" height="11" viewBox="0 0 10 11"><path d="M2 8V5a3 3 0 0 1 6 0v3l1 1H1z M4 10h2" fill="none" stroke="#aaa" stroke-width=".8"/></svg></div>
    <div class="avatar" role="img" aria-label="User profile photo"></div>
    <div class="avatar-dot"></div>
    <svg class="chev" width="10" height="6" viewBox="0 0 10 6"><path d="M1 1l4 4 4-4" fill="none" stroke="#888" stroke-width="1"/></svg>
  </header>

  <section class="org-card left">
    <div class="org-logo" style="left:22px">Northway</div>
    <div class="org-info" style="left:132px">
      <div class="org-name">NWLDEMO19</div>
      <div class="org-sub">Students</div>
      <div class="org-status"><span class="info-box">i</span>Status: No record found</div>
      <div class="btn-add"><svg width="12" height="12"><path d="M6 0v12M0 6h12" stroke="#fff" stroke-width="2"/></svg>Add Student via...<span class="caret"></span></div>
    </div>
  </section>

  <section class="org-card right">
    <div class="org-logo" style="left:25px">RCVTS</div>
    <div class="org-info" style="left:139px">
      <div class="org-name">RCVTS</div>
      <div class="org-sub">Students</div>
      <div class="org-status"><span class="info-box">i</span>Status: No record found</div>
      <div class="btn-add"><svg width="12" height="12"><path d="M6 0v12M0 6h12" stroke="#fff" stroke-width="2"/></svg>Add Student via...<span class="caret"></span></div>
    </div>
  </section>

  <div class="section-label">Students</div>

  <section class="students-panel">
    <h2 class="panel-title">GradeLedgerDemoTest</h2>
    <div class="search"><svg width="16" height="16" viewBox="0 0 16 16"><circle cx="6.5" cy="6.5" r="5" fill="none" stroke="#999"/><path d="M10 10l5 5" stroke="#999"/></svg>tesdt...</div>
    <div class="filter">School/Building <svg width="9" height="5" viewBox="0 0 9 5"><path d="M.5.5l4 4 4-4" fill="none" stroke="#777"/></svg></div>
    <div class="btn-add"><svg width="12" height="12"><path d="M6 0v12M0 6h12" stroke="#fff" stroke-width="2"/></svg>Add Student via...<span class="caret"></span></div>

    <div class="table">
      <div class="row head">
        <span class="cell c-name">Name</span><span class="cell c-grade">Grade</span><span class="cell c-year">Year</span><span class="cell c-school">School/Building</span><span class="cell c-act" style="top:12px">Actions</span>
      </div>
      <div class="row" style="height:53px">
        <span class="cell c-name" style="top:24px">NWVIEW8108 Testing</span><span class="cell c-grade" style="top:11px">KG</span><span class="cell c-school" style="top:15px">testing</span><span class="cell c-act" style="top:10px"><span class="btn-edit">Create/Edit...</span></span>
      </div>
      <div class="row hl" style="height:52px">
        <span class="cell c-name" style="top:24px">Dana Whitfield</span><span class="cell c-grade" style="top:20px">11</span><span class="cell c-school" style="top:10px">tesdt</span><span class="cell c-act" style="top:10px"><span class="btn-edit">Create/Edit...</span></span>
      </div>
      <div class="row" style="height:51px">
        <span class="cell c-name" style="top:19px">Harlan J Whitfield</span><span class="cell c-act" style="top:8px"><span class="btn-edit">Create/Edit...</span></span>
      </div>
      <div class="row" style="height:55px">
        <span class="cell c-name" style="top:25px">REGRESSION TEST TEST</span><span class="cell c-act" style="top:7px"><span class="btn-edit">Create/Edit...</span></span>
      </div>
      <div class="row" style="height:48px">
        <span class="cell c-name" style="top:18px">test test</span><span class="cell c-grade" style="top:14px">09</span><span class="cell c-year" style="top:18px">2024</span><span class="cell c-school" style="top:18px">Maple Ridge High School</span><span class="cell c-act" style="top:6px"><span class="btn-edit">Create/Edit...</span></span>
      </div>
      <div class="row" style="height:58px">
        <span class="cell c-name" style="top:17px">Milo Grant Porter</span><span class="cell c-act" style="top:11px"><span class="btn-edit">Create/Edit...</span></span>
      </div>
    </div>
  </section>

  <div class="pager">
    <svg width="11" height="12"><path d="M11 0v12L0 6z" fill="#3d97ad"/></svg>
    <span>1</span>
    <svg width="11" height="12"><path d="M0 0v12l11-6z" fill="#3d97ad"/></svg>
    <span>of 44</span>
  </div>
</div>
</body>
</html>
```